Freelancers in the field of IT security and IT service need a business card design

I need a business card design for my company. I am a freelancer and active in the area of IT security, IT support% 26 # 252; tung, consulting. I am not yet color-coded, but it should be a modern color that can also be used for a later website. The design should be innovation. Exude dynamism and reliability

Target Market(s)

IT security, IT solutions

Contact Information for Business Card

Firma: brunov-consulting, Inhaber: Lukas Brunov
Adresse: Lindenhof 4, D-73618 Brenzfeld
Telefon: +49 (0) 5137 640928
E-Mail Lukas.Brunov@brunov-consulting.example

```html
<!DOCTYPE html>
<html lang="de">
<head>
<meta charset="utf-8">
<title>brunov-consulting – Visitenkarte</title>
<link rel="stylesheet" href="https://fonts.googleapis.com/css2?family=Mulish:wght@300;400;700&display=swap">
<style>
  :root {
    --brand-blue: #0d3f8f;
    --card-white: #f3f3f3;
    --text-grey: #3a3a3a;
    --stage: #e4e4e2;
    --white: #ffffff;
  }
  * { margin: 0; padding: 0; box-sizing: border-box; }
  html, body {
    width: 1200px; height: 960px; overflow: hidden;
    background: var(--stage);
    font-family: "Mulish", sans-serif;
  }
  .stage {
    width: 1200px; height: 960px;
    display: flex; flex-direction: column; align-items: center;
    justify-content: center; gap: 48px;
  }
  .card {
    position: relative;
    width: 680px; height: 416px;
    box-shadow: 0 6px 20px rgba(0,0,0,0.12);
    overflow: hidden;
  }
  .card--front {
    background: var(--brand-blue);
    display: flex; align-items: center; justify-content: center;
  }
  .wordmark {
    font-weight: 300;
    letter-spacing: 0.5px;
  }
  .card--front .wordmark { color: var(--white); font-size: 40px; }

  .card--back { background: var(--card-white); }
  .card--back .wordmark {
    position: absolute; left: 58px; top: 196px;
    color: var(--brand-blue); font-size: 33px;
  }
  .divider {
    position: absolute; left: 372px; top: 138px;
    width: 2px; height: 136px; background: var(--brand-blue);
  }
  .contact {
    position: absolute; left: 392px; top: 140px;
    color: var(--text-grey);
  }
  .contact__name {
    color: var(--brand-blue); font-weight: 700; font-size: 21px; line-height: 1.1;
  }
  .contact__role { font-size: 11px; margin: 2px 0 16px 14px; }
  .contact__list { list-style: none; margin-left: 22px; }
  .contact__item {
    display: flex; align-items: center; gap: 8px;
    font-size: 11px; line-height: 1; margin-bottom: 9px;
  }
  .contact__item svg { width: 11px; height: 11px; flex: none; }
  .band {
    position: absolute; left: 0; right: 0; bottom: 0;
    height: 14px; background: var(--brand-blue);
  }
</style>
</head>
<body>
<main class="stage">
  <section class="card card--front" aria-label="Vorderseite">
    <span class="wordmark">brunov-consulting</span>
  </section>

  <section class="card card--back" aria-label="Rückseite">
    <span class="wordmark">brunov-consulting</span>
    <div class="divider"></div>
    <div class="contact">
      <p class="contact__name">Lukas Brunov</p>
      <p class="contact__role">Inhaber</p>
      <ul class="contact__list">
        <li class="contact__item">
          <svg viewBox="0 0 12 12" aria-hidden="true"><path d="M6 1a3.5 3.5 0 0 0-3.5 3.5C2.5 7 6 11 6 11s3.5-4 3.5-6.5A3.5 3.5 0 0 0 6 1z" fill="none" stroke="var(--brand-blue)" stroke-width="1.3"/><circle cx="6" cy="4.5" r="1.2" fill="var(--brand-blue)"/></svg>
          Lindenhof 4, D-73618 Brenzfeld
        </li>
        <li class="contact__item">
          <svg viewBox="0 0 12 12" aria-hidden="true"><path d="M3 1.5l1.8 2.2-1 1.2a6 6 0 0 0 3.3 3.3l1.2-1 2.2 1.8-1 1.5C5.5 10.5 1.5 6.5 1.5 2.5z" fill="var(--brand-blue)"/></svg>
          +49 (0) 5137 640928
        </li>
        <li class="contact__item">
          <svg viewBox="0 0 12 12" aria-hidden="true"><rect x="1" y="2.5" width="10" height="7" fill="var(--brand-blue)"/><path d="M1 2.5l5 4 5-4" fill="none" stroke="var(--white)" stroke-width="1"/></svg>
          Lukas.Brunov@brunov-consulting.example
        </li>
      </ul>
    </div>
    <div class="band"></div>
  </section>
</main>
</body>
</html>
```